Cafe Menu Required

We need a menu for our coffee shop.
I would like something very much the same as what I have attached.

I have attached a word doc with the items needed on the menu.

I have also attached our logo

I would like to print these on A3 size poster

Industry/Entity Type

Cafe

```html
<!DOCTYPE html>
<html lang="en">
<head>
<meta charset="utf-8">
<title>NOOK – Cafe Menu</title>
<link rel="stylesheet" href="https://fonts.googleapis.com/css2?family=Open+Sans:wght@700&family=Arimo:wght@400;700&display=swap">
<style>
  :root {
    --backdrop: #8c8c8c;
    --brown: #7b4521;
    --brown-dark: #6a3a1a;
    --cream-light: #fdf3e4;
    --cream-deep: #fcd998;
    --title-ink: #2f2f2f;
    --brand-red: #e21b3c;
    --white: #ffffff;
    --photo-warm: #a57a55;
    --photo-light: #e9e3da;
  }
  * { margin: 0; padding: 0; box-sizing: border-box; }
  html, body { width: 870px; height: 1200px; overflow: hidden; background: var(--backdrop); }
  .canvas { position: relative; width: 870px; height: 1200px; }
  .poster {
    position: absolute; left: 37px; top: 37px; width: 796px; height: 1126px;
    background: var(--brown); overflow: hidden;
  }
  .wave { position: absolute; left: 0; width: 796px; }
  .wave--top { top: 0; }
  .wave--bottom { bottom: 0; }

  .banner {
    position: absolute; left: 0; top: 106px; width: 796px; height: 84px;
    background: linear-gradient(90deg, var(--cream-light) 0%, #fdeccf 40%, var(--cream-deep) 100%);
  }
  .banner__title {
    position: absolute; left: 278px; top: 0; height: 84px; line-height: 84px;
    font: 700 22.5px "Open Sans", sans-serif; color: var(--title-ink); letter-spacing: 0.3px;
  }
  .brand {
    position: absolute; left: 52px; top: 106px; height: 84px;
    display: flex; align-items: center; gap: 12px;
  }
  .brand__dot { width: 44px; height: 44px; border-radius: 50%; background: var(--brand-red); }
  .brand__name { font: 700 42px "Arimo", sans-serif; color: var(--brand-red); letter-spacing: 1px; }

  .section-title {
    position: absolute; color: var(--white); text-align: center;
    font: 700 16px "Arimo", sans-serif; letter-spacing: 0.3px;
  }
  .section-title--light { font-weight: 400; }

  .menu { position: absolute; list-style: none; color: var(--white); font: 400 16px "Arimo", sans-serif; }
  .menu li { display: flex; align-items: baseline; white-space: nowrap; }
  .menu .leader {
    flex: 1; height: 1em; margin: 0 4px;
    background-image: radial-gradient(circle, var(--white) 0.9px, transparent 1.3px);
    background-size: 6.6px 4px; background-repeat: repeat-x; background-position: left bottom 2px;
  }
  .menu--hot { left: 31px; top: 329px; width: 328px; }
  .menu--hot li { height: 32.5px; }
  .menu--side { left: 417px; width: 328px; font-size: 15.5px; }
  .menu--side li { height: 24.4px; }
  .menu--extras { top: 541px; }
  .menu--cold { top: 734px; }

  .photo {
    position: absolute; border: 6px solid var(--white);
    box-shadow: 0 3px 8px rgba(0,0,0,0.35);
  }
  .photo--cup {
    left: 412px; top: 234px; width: 290px; height: 196px; transform: rotate(8deg);
    background: radial-gradient(ellipse at 55% 55%, var(--photo-light) 0%, #cfc4b6 45%, var(--photo-warm) 100%);
  }
  .photo--beans {
    left: 44px; top: 838px; width: 320px; height: 220px; transform: rotate(-8deg);
    background: radial-gradient(ellipse at 60% 50%, var(--photo-light) 0%, #c9ab8a 40%, #6d4527 100%);
  }

  .social {
    position: absolute; left: 436px; top: 925px; width: 340px; text-align: center;
    color: var(--white); font: 400 38px/44px "Arimo", sans-serif;
  }
</style>
</head>
<body>
<div class="canvas">
  <div class="poster">
    <svg class="wave wave--top" height="50" viewBox="0 0 796 50" aria-hidden="true">
      <path d="M0 0 H796 V30 C760 44 730 44 700 32 C660 16 620 16 580 30 C540 44 500 44 460 30 C420 16 380 16 340 30 C300 44 260 44 220 30 C180 16 140 16 100 30 C60 44 30 44 0 32 Z" fill="var(--brown-dark)"/>
    </svg>

    <div class="banner"><span class="banner__title">COFFEE – CATERING – FOOD TO GO</span></div>
    <div class="brand"><span class="brand__dot"></span><span class="brand__name">NOOK</span></div>

    <div class="section-title" style="left:31px; top:266px; width:356px;">HOT BEVERAGES</div>
    <ul class="menu menu--hot">
      <li>Espresso<span class="leader"></span>3.5</li>
      <li>Piccolo<span class="leader"></span>3.5</li>
      <li>Short Macchiato<span class="leader"></span>4.0</li>
      <li>Long Macchiato<span class="leader"></span>4.5</li>
      <li>Latte<span class="leader"></span>4/4.5/5.5</li>
      <li>Cappucinno<span class="leader"></span>4/4.5/5.5</li>
      <li>Flat White<span class="leader"></span>4/4.50/5.50</li>
      <li>Long Black<span class="leader"></span>4/4.50/5.50</li>
      <li>Hot Chocolate<span class="leader"></span>4/4.50/5.50</li>
      <li>White Hot Chocolate<span class="leader"></span>4/4.50/5.50</li>
      <li>Mocha<span class="leader"></span>4.5/5.0/6.0</li>
      <li>White Choc Mocha<span class="leader"></span>4.5/5.0/6.0</li>
      <li>Chai Latte<span class="leader"></span>4.5/5.0/6.0</li>
      <li>Dirty Chai<span class="leader"></span>5.0/5.5/6.5</li>
      <li>Selection of Teas<span class="leader"></span>3.8</li>
    </ul>

    <div class="photo photo--cup" role="img" aria-label="Photo of a cappuccino in a white cup on a saucer"></div>

    <div class="section-title" style="left:417px; top:494px; width:352px;">EXTRAS</div>
    <ul class="menu menu--side menu--extras">
      <li>Extra Shot<span class="leader"></span>0.5</li>
      <li>Decaf<span class="leader"></span>0.5</li>
      <li>Syrups – Caramel/Hazelnut/Vanilla<span class="leader"></span>0.5</li>
      <li>Soy<span class="leader"></span>0.5</li>
      <li>Lactose free<span class="leader"></span>0.5</li>
    </ul>

    <div class="section-title section-title--light" style="left:417px; top:688px; width:352px;">COLD BEVERAGES</div>
    <ul class="menu menu--side menu--cold">
      <li>Iced Latte<span class="leader"></span>4.5</li>
      <li>Iced Long Black<span class="leader"></span>4.5</li>
      <li>Iced Coffee w/ice cream<span class="leader"></span>6.0</li>
      <li>Iced Chocolate w/ice cream<span class="leader"></span>6.0</li>
      <li>Coffee Frappe<span class="leader"></span>6.0</li>
      <li>Mango Frappe<span class="leader"></span>6.0</li>
    </ul>

    <div class="photo photo--beans" role="img" aria-label="Photo of an espresso cup beside a sack of coffee beans"></div>

    <p class="social">Your Facepage<br>and<br>chirper link here</p>

    <svg class="wave wave--bottom" height="70" viewBox="0 0 796 70" aria-hidden="true">
      <path d="M0 20 C40 6 70 6 110 20 C150 34 190 34 230 20 C270 6 310 6 350 20 C390 34 430 34 470 20 C510 6 550 6 590 20 C630 34 670 34 710 20 C740 10 770 10 796 18 V70 H0 Z" fill="var(--brown-dark)"/>
    </svg>
  </div>
</div>
</body>
</html>
```